Powerpoint design for spirits and cosmetics packaging company

We need a powerpoint template that will be used for company presentations, projects, award ceremonies etc... We are packaging in the wine and spirits sector as well as in the cosmetics sector. Our job is to package our customers' bottles in gift boxes, to carry out labeling, quality control, etc. We are based in Cognac.
We work for the big names in luxury: QDKT, Valtore Mison, Fulvesta, Brunelle etc...
The template should be neat with at least 10 different slides.
Cover page, summary page, product description page (several), page including a schedule, price presentation page.

Target Market(s)

premium spirits and cosmetics

Industry/Entity Type

Spiritueux et cosmétique

Font styles to use
Sans Serif

Requirements
Must have
• My project must have the logo attached, the possibility to add / modify photos afterwards. Must have about ten different slides

```html
<!DOCTYPE html>
<html lang="en">
<head>
<meta charset="utf-8">
<title>Maison Verlaine – Presentation Template</title>
<link href="https://fonts.googleapis.com/css2?family=Roboto:wght@400;500;700;900&display=swap" rel="stylesheet">
<style>
:root{
  --page:#efefef;
  --white:#ffffff;
  --crimson:#d2103d;
  --red:#e01f3d;
  --orange:#f7931e;
  --coral:#e94b3a;
  --ink:#111111;
  --text:#333333;
  --muted:#777777;
  --pink:#f7dfe1;
  --card:#f0f0f3;
  --line:#e2e2e2;
}
*{margin:0;padding:0;box-sizing:border-box}
html,body{width:1200px;height:3955px;overflow:hidden}
body{background:var(--page);font-family:'Roboto',Arial,sans-serif;color:var(--text);position:relative}
.slide{position:absolute;left:103px;width:996px;height:560px;background:var(--white);overflow:hidden;box-shadow:0 2px 6px rgba(0,0,0,.08)}
.abs{position:absolute}

/* brand block */
.brand{position:absolute;display:flex;gap:12px;align-items:flex-start}
.brand-square{width:46px;height:46px;background:var(--crimson);margin-top:4px}
.brand-name{font-size:21px;font-weight:500;line-height:1.05;letter-spacing:1.5px;color:var(--crimson);text-transform:uppercase}
.brand-tag{font-size:10px;letter-spacing:1px;color:var(--orange);text-transform:uppercase;line-height:1.3;margin-top:3px}
.brand.light .brand-square{background:var(--white)}
.brand.light .brand-name,.brand.light .brand-tag{color:var(--white)}

.slide-title{position:absolute;right:116px;top:38px;font-size:27px;font-weight:700;color:var(--ink);letter-spacing:.5px}
.corner-flag{position:absolute;right:52px;top:15px;width:42px;height:82px}
.footer-band{position:absolute;left:0;right:0;bottom:0;height:38px;background:linear-gradient(180deg,var(--orange),#ee5a24);color:var(--white);font-size:10px;text-align:center;line-height:38px}
.body-copy{font-size:12.5px;line-height:20.7px;color:var(--text);text-align:justify}
.body-copy p+p{margin-top:10px}

/* cover */
.cover-photo{position:absolute;inset:0;background:radial-gradient(ellipse at 50% 40%,#6b5a48 0%,#3b3430 45%,#1d1b1a 100%)}
.cover-title{position:absolute;left:0;right:0;text-align:center;color:var(--white);text-shadow:0 2px 6px rgba(0,0,0,.5)}
.cover-welcome{top:289px;font-size:30px;font-weight:700}
.cover-name{top:338px;font-size:58px;font-weight:900;letter-spacing:1px}
.cover-sub{top:420px;font-size:26px;letter-spacing:9px;font-weight:400}
.socials{position:absolute;top:475px;left:0;right:0;display:flex;justify-content:center;gap:8px}
.socials span{width:20px;height:20px;border:1.5px solid rgba(255,255,255,.8);border-radius:50%}

/* about */
.about-photo-shadow{position:absolute;left:65px;top:133px;width:413px;height:343px;background:var(--crimson)}
.about-photo{position:absolute;left:51px;top:121px;width:417px;height:301px;background:linear-gradient(135deg,#c9b59a,#8a4a1f 55%,#3b3d46)}

/* spirits */
.section-title{position:absolute;left:48px;top:152px;font-size:27px;font-weight:700;color:var(--ink)}
.pink-panel{position:absolute;left:734px;top:0;width:262px;height:560px;background:var(--pink)}
.photo-a{position:absolute;left:550px;top:23px;width:324px;height:244px;border-radius:0 30px 0 30px;background:linear-gradient(135deg,#8a8f6a,#5a3a22 50%,#2f3d2a)}
.photo-b{position:absolute;left:550px;top:293px;width:324px;height:244px;border-radius:30px 0 30px 0;background:linear-gradient(135deg,#3a4a66,#9aa4b8 50%,#d66a2a)}

/* schedule */
.timeline{position:absolute;left:0;top:0}
.year{position:absolute;width:290px}
.year-dot{position:absolute;left:0;top:0;width:20px;height:20px;border-radius:50%;background:var(--white);border:4px solid currentColor;box-shadow:0 0 0 3px #f3f3f3}
.year-dot::after{content:"";position:absolute;inset:1px;border-radius:50%;background:currentColor}
.year-pill{position:absolute;left:33px;top:-2px;width:90px;height:25px;border-radius:13px;background:currentColor}
.year-pill b{position:absolute;left:17px;top:4px;color:var(--white);font-size:14px;font-weight:700}
.year-pill i{position:absolute;right:4px;top:4px;width:17px;height:17px;border-radius:50%;background:var(--white)}
.year h4{position:absolute;top:30px;font-size:10px;font-weight:700;color:var(--ink);white-space:nowrap}
.year ul{position:absolute;top:56px;list-style:none;font-size:9px;color:#444}
.year li{height:18.3px;display:flex;align-items:center;gap:7px;white-space:nowrap}
.tick{width:9px;height:9px;border-radius:50%;background:currentColor;flex:none;position:relative}
.tick::after{content:"";position:absolute;left:2.5px;top:1.6px;width:2.5px;height:4px;border:solid #fff;border-width:0 1.2px 1.2px 0;transform:rotate(45deg)}
.red{color:var(--crimson)}
.orange{color:var(--orange)}
.coral{color:var(--coral)}

/* pricing */
.plan{position:absolute;top:140px;width:204px;height:337px}
.plan-card{position:absolute;left:0;top:0;width:204px;height:268px;background:var(--card);border-radius:10px 10px 0 0}
.plan-ribbon{position:absolute;left:-28px;top:14px;width:260px;height:52px}
.plan-ribbon span{position:absolute;left:28px;top:0;width:204px;height:32px;line-height:32px;text-align:center;color:var(--white);font-weight:700;font-size:17px}
.price{position:absolute;left:65px;top:72px;width:74px;height:74px;border-radius:50%;background:currentColor;box-shadow:0 0 0 7px var(--white),0 0 0 8px #e6e6e6}
.price b{position:absolute;inset:0;text-align:center;line-height:74px;color:var(--white);font-size:27px;font-weight:700}
.plan ul{position:absolute;left:22px;top:158px;list-style:none;font-size:10.5px;color:#333}
.plan li{height:20.5px;display:flex;align-items:center;gap:8px}
.plan-btn{position:absolute;left:0;top:268px;width:204px;height:69px}
.plan-btn span{position:absolute;left:0;right:0;top:14px;text-align:center;color:var(--white);font-size:14px;font-weight:700;display:flex;justify-content:center;align-items:center;gap:8px}
.plan-btn i{width:13px;height:13px;border-radius:50%;background:var(--white);position:relative}
.plan-btn i::after{content:"";position:absolute;left:3px;top:4px;width:4px;height:4px;border:solid currentColor;border-width:1.5px 1.5px 0 0;transform:rotate(45deg)}

/* thank you */
.thanks-photo{position:absolute;left:0;top:0;width:550px;height:560px;background:radial-gradient(ellipse at 45% 55%,#b2621f 0%,#5e3a20 45%,#23302c 100%)}
.thanks-word{position:absolute;left:0;width:550px;text-align:center;color:var(--white);font-weight:900;line-height:1}
.contact-photo{position:absolute;left:550px;top:300px;width:446px;height:260px;background:linear-gradient(180deg,rgba(255,255,255,0),#ececec 60%,#e4e4e4)}
.contact{position:absolute;left:596px;width:380px;display:flex;align-items:center;gap:24px}
.contact-icon{width:46px;height:46px;border-radius:50%;background:var(--crimson);display:flex;align-items:center;justify-content:center;flex:none;box-shadow:0 0 0 5px rgba(210,16,61,.12)}
.contact-text{font-size:13px;color:var(--ink);font-weight:500;line-height:20px}
</style>
</head>
<body>

<!-- Cover -->
<section class="slide" style="top:89px">
  <div class="cover-photo" role="img" aria-label="Photo of a rum bottle on a packing line in a workshop"></div>
  <div class="brand light" style="left:51px;top:28px">
    <div class="brand-square"></div>
    <div><div class="brand-name">Maison<br>Verlaine</div><div class="brand-tag">Co-packing<br>services</div></div>
  </div>
  <div class="cover-title cover-welcome">WELCOME TO</div>
  <div class="cover-title cover-name">MAISON VERLAINE</div>
  <div class="cover-title cover-sub">CO- PACKING SERVICES</div>
  <div class="socials"><span></span><span></span><span></span><span></span></div>
</section>

<!-- About -->
<section class="slide" style="top:732px">
  <div class="brand" style="left:46px;top:16px">
    <div class="brand-square"></div>
    <div><div class="brand-name">Maison<br>Verlaine</div><div class="brand-tag">Co-packing<br>services</div></div>
  </div>
  <h2 class="slide-title">ABOUT US</h2>
  <svg class="corner-flag" viewBox="0 0 42 82"><defs><linearGradient id="fg1" x1="0" y1="0" x2="1" y2="1"><stop offset="0" stop-color="#f2586a"/><stop offset="1" stop-color="#d2103d"/></linearGradient></defs><path d="M42 0V82L0 41Z" fill="url(#fg1)"/></svg>
  <div class="about-photo-shadow"></div>
  <div class="about-photo" role="img" aria-label="Photo of hands cleaning an amber spirits decanter"></div>
  <div class="body-copy abs" style="left:531px;top:158px;width:414px">
    <p>Lorem ipsum dolor sit amet, consectetur adipiscing elit, sed do eiusmod tempor incididunt ut labore et dolore magna aliqua. Ut enim ad minim veniam, quis nostrud exercitation ullamco laboris nisi ut aliquip ex ea commodo consequat. Duis aute irure dolor in reprehenderit in voluptate velit esse cillum dolore eu fugiat nulla pariatur. Excepteur sint occaecat cupidatat non proident, sunt in culpa qui officia deserunt mollit anim id est laborum.</p>
    <p>Lorem ipsum dolor sit amet, consectetur adipiscing elit, sed do eiusmod tempor incididunt ut labore et dolore magna aliqua. Ut enim ad minim veniam, quis nostrud exercitation ullamco laboris nisi ut aliquip ex ea commodo consequat. Duis aute irure dolor in reprehenderit in voluptate velit esse cillum dolore eu fugiat nulla pariatur. Excepteur sint occaecat cupidatat non proident, sunt in culpa qui officia deserunt mollit anim id est laborum."</p>
  </div>
  <div class="footer-band">© 2023 Maison Verlaine. All Rights Reserved</div>
</section>

<!-- Spirits and cosmetics -->
<section class="slide" style="top:1375px">
  <div class="pink-panel"></div>
  <svg class="abs" style="left:660px;top:0" width="200" height="40" viewBox="0 0 200 40"><path d="M0 2 Q90 -6 200 40" fill="none" stroke="#d2103d" stroke-width="2.5"/></svg>
  <div class="abs" style="left:788px;top:530px;width:4px;height:30px;background:var(--crimson)"></div>
  <div class="brand" style="left:51px;top:32px">
    <div class="brand-square"></div>
    <div><div class="brand-name">Maison<br>Verlaine</div><div class="brand-tag">Co-packing<br>services</div></div>
  </div>
  <h2 class="section-title">SPIRITS AND COSMETICS</h2>
  <div class="body-copy abs" style="left:51px;top:197px;width:416px">
    <p>Lorem ipsum dolor sit amet, consectetur adipiscing elit, sed do eiusmod tempor incididunt ut labore et dolore magna aliqua. Ut enim ad minim veniam, quis nostrud exercitation ullamco laboris nisi ut aliquip ommodo consequat. Duis aute irure dolor in reprehenderit in voluptate velit esse cillum dolore eu fugiat nulla pariatur. Excepteur sint occaecat cupidatat non proident, sunt in culpa qui officia deserunt mollit anim id est laborum.</p>
    <p>Lorem ipsum dolor sit amet, consectetur adipiscing elit, sed do eiusmod tempor incididunt ut labore et dolore magna aliqua. Ut enim ad minim veniam, quis nostrud exercitation ullamco laboris nisi ut aliquip ommodo consequat. Duis aute irure dolor in reprehenderit in voluptate velit esse cillum dolore eu fugiat nulla pariatur. Excepteur sint occaecat cupidatat non proident, sunt in culpa qui officia deserunt mollit anim id est laborum.</p>
  </div>
  <div class="photo-a" role="img" aria-label="Photo of hands labelling a cognac bottle"></div>
  <div class="photo-b" role="img" aria-label="Photo of a worker packing clear glass bottles into cartons"></div>
</section>

<!-- Schedule -->
<section class="slide" style="top:2018px">
  <div class="brand" style="left:46px;top:16px">
    <div class="brand-square"></div>
    <div><div class="brand-name">Maison<br>Verlaine</div><div class="brand-tag">Co-packing<br>services</div></div>
  </div>
  <h2 class="slide-title">SCHEDULE</h2>
  <svg class="corner-flag" viewBox="0 0 42 82"><defs><linearGradient id="fg2" x1="0" y1="0" x2="1" y2="1"><stop offset="0" stop-color="#f2586a"/><stop offset="1" stop-color="#d2103d"/></linearGradient></defs><path d="M42 0V82L0 41Z" fill="url(#fg2)"/></svg>
  <svg class="timeline" width="996" height="560" viewBox="0 0 996 560">
    <path d="M74 154 H862 A82 82 0 0 1 862 319 H74 A82 86 0 0 0 74 491 H880" fill="none" stroke="#e4e4e4" stroke-width="1.5"/>
  </svg>

  <div class="year red" style="left:64px;top:144px">
    <div class="year-dot"></div><div class="year-pill"><b>2018</b><i></i></div>
    <h4 style="left:0">Revive of a Large Project</h4>
    <ul style="left:0"><li><span class="tick"></span>Lorem ipsum dolor sit amet</li><li><span class="tick"></span>Lorem ipsum dolor sit amet</li><li><span class="tick"></span>Lorem ipsum dolor sit amet</li><li><span class="tick"></span>Lorem ipsum dolor sit amet</li></ul>
  </div>
  <div class="year orange" style="left:354px;top:144px">
    <div class="year-dot"></div><div class="year-pill"><b>2019</b><i></i></div>
    <h4 style="left:0">Large Transformation project</h4>
    <ul style="left:0"><li><span class="tick"></span>Lorem ipsum dolor sit amet</li><li><span class="tick"></span>Lorem ipsum dolor sit amet</li><li><span class="tick"></span>Lorem ipsum dolor sit amet</li><li><span class="tick"></span>Lorem ipsum dolor sit amet</li></ul>
  </div>
  <div class="year red" style="left:645px;top:144px">
    <div class="year-dot"></div><div class="year-pill"><b>2020</b><i></i></div>
    <h4 style="left:0">Large joint project with 3 clients</h4>
    <ul style="left:0"><li><span class="tick"></span>Lorem ipsum dolor sit amet</li><li><span class="tick"></span>Lorem ipsum dolor sit amet</li><li><span class="tick"></span>Lorem ipsum dolor sit amet</li><li><span class="tick"></span>Lorem ipsum dolor sit amet</li></ul>
  </div>

  <div class="year orange" style="left:64px;top:310px">
    <div class="year-dot"></div><div class="year-pill"><b>2021</b><i></i></div>
    <h4 style="left:46px">Critical Transformation project</h4>
    <ul style="left:46px"><li>Lorem ipsum dolor sit amet<span class="tick"></span></li><li>Lorem ipsum dolor sit amet<span class="tick"></span></li><li>Lorem ipsum dolor sit amet<span class="tick"></span></li><li>Lorem ipsum dolor sit amet<span class="tick"></span></li></ul>
  </div>
  <div class="year red" style="left:354px;top:310px">
    <div class="year-dot"></div><div class="year-pill"><b>2022</b><i></i></div>
    <h4 style="left:30px">Largest joint project with 11 clients</h4>
    <ul style="left:46px"><li>Lorem ipsum dolor sit amet<span class="tick"></span></li><li>Lorem ipsum dolor sit amet<span class="tick"></span></li><li>Lorem ipsum dolor sit amet<span class="tick"></span></li><li>Lorem ipsum dolor sit amet<span class="tick"></span></li></ul>
  </div>
  <div class="year orange" style="left:645px;top:310px">
    <div class="year-dot"></div><div class="year-pill"><b>2023</b><i></i></div>
    <h4 style="left:60px">Unternehmens-gründung</h4>
    <ul style="left:46px"><li>Lorem ipsum dolor sit amet<span class="tick"></span></li><li>Lorem ipsum dolor sit amet<span class="tick"></span></li><li>Lorem ipsum dolor sit amet<span class="tick"></span></li><li>Lorem ipsum dolor sit amet<span class="tick"></span></li></ul>
  </div>
  <div class="footer-band">© 2023 Maison Verlaine. All Rights Reserved</div>
</section>

<!-- Price presentation -->
<section class="slide" style="top:2661px">
  <div class="brand" style="left:46px;top:16px">
    <div class="brand-square"></div>
    <div><div class="brand-name">Maison<br>Verlaine</div><div class="brand-tag">Co-packing<br>services</div></div>
  </div>
  <h2 class="slide-title">PRICE PRESENTATION</h2>
  <svg class="corner-flag" viewBox="0 0 42 82"><defs><linearGradient id="fg3" x1="0" y1="0" x2="1" y2="1"><stop offset="0" stop-color="#f2586a"/><stop offset="1" stop-color="#d2103d"/></linearGradient></defs><path d="M42 0V82L0 41Z" fill="url(#fg3)"/></svg>

  <div class="plan orange" style="left:94px">
    <div class="plan-card"></div>
    <svg class="plan-ribbon" viewBox="0 0 260 52"><path d="M0 8H28V42H8L14 25Z" fill="currentColor" opacity=".8"/><path d="M260 8H232V42H252L246 25Z" fill="currentColor" opacity=".8"/><path d="M28 32L40 46V32Z M232 32L220 46V32Z" fill="#000" opacity=".25"/><rect x="28" y="0" width="204" height="32" fill="currentColor"/></svg>
    <div class="plan-ribbon"><span>BASIC</span></div>
    <div class="price"><b>$78</b></div>
    <ul><li><span class="tick red"></span>Lorem ipsum dolor sit amet</li><li><span class="tick red"></span>Lorem ipsum dolor sit amet</li><li><span class="tick red"></span>Lorem ipsum dolor sit amet</li><li><span class="tick red"></span>Lorem ipsum dolor sit amet</li></ul>
    <svg class="plan-btn" viewBox="0 0 204 69"><path d="M0 0H204V48L102 69L0 48Z" fill="currentColor"/></svg>
    <div class="plan-btn"><span>LEARN MORE <i class="orange"></i></span></div>
  </div>

  <div class="plan red" style="left:396px">
    <div class="plan-card"></div>
    <svg class="plan-ribbon" viewBox="0 0 260 52"><path d="M0 8H28V42H8L14 25Z" fill="currentColor" opacity=".8"/><path d="M260 8H232V42H252L246 25Z" fill="currentColor" opacity=".8"/><path d="M28 32L40 46V32Z M232 32L220 46V32Z" fill="#000" opacity=".25"/><rect x="28" y="0" width="204" height="32" fill="currentColor"/></svg>
    <div class="plan-ribbon"><span>STANDARD</span></div>
    <div class="price"><b>$78</b></div>
    <ul><li><span class="tick red"></span>Lorem ipsum dolor sit amet</li><li><span class="tick red"></span>Lorem ipsum dolor sit amet</li><li><span class="tick red"></span>Lorem ipsum dolor sit amet</li><li><span class="tick red"></span>Lorem ipsum dolor sit amet</li></ul>
    <svg class="plan-btn" viewBox="0 0 204 69"><path d="M0 0H204V48L102 69L0 48Z" fill="currentColor"/></svg>
    <div class="plan-btn"><span>LEARN MORE <i class="red"></i></span></div>
  </div>

  <div class="plan coral" style="left:697px">
    <div class="plan-card"></div>
    <svg class="plan-ribbon" viewBox="0 0 260 52"><path d="M0 8H28V42H8L14 25Z" fill="currentColor" opacity=".8"/><path d="M260 8H232V42H252L246 25Z" fill="currentColor" opacity=".8"/><path d="M28 32L40 46V32Z M232 32L220 46V32Z" fill="#000" opacity=".25"/><rect x="28" y="0" width="204" height="32" fill="currentColor"/></svg>
    <div class="plan-ribbon"><span>PREMIUM</span></div>
    <div class="price"><b>$78</b></div>
    <ul><li><span class="tick red"></span>Lorem ipsum dolor sit amet</li><li><span class="tick red"></span>Lorem ipsum dolor sit amet</li><li><span class="tick red"></span>Lorem ipsum dolor sit amet</li><li><span class="tick red"></span>Lorem ipsum dolor sit amet</li></ul>
    <svg class="plan-btn" viewBox="0 0 204 69"><path d="M0 0H204V48L102 69L0 48Z" fill="currentColor"/></svg>
    <div class="plan-btn"><span>LEARN MORE <i class="coral"></i></span></div>
  </div>
  <div class="footer-band">© 2023 Maison Verlaine. All Rights Reserved</div>
</section>

<!-- Thank you -->
<section class="slide" style="top:3305px">
  <div class="thanks-photo" role="img" aria-label="Photo of hands holding a cognac bottle"></div>
  <div class="abs" style="left:95px;top:163px;width:379px;height:4px;background:var(--crimson)"></div>
  <div class="abs" style="left:277px;top:158px;width:14px;height:14px;border-radius:50%;background:var(--crimson)"></div>
  <div class="thanks-word" style="top:188px;font-size:104px">THANK</div>
  <div class="thanks-word" style="top:278px;font-size:104px">YOU</div>
  <div class="abs" style="left:95px;top:386px;width:379px;height:4px;background:var(--crimson)"></div>

  <div class="contact-photo" role="img" aria-label="Faded photo of a delivery truck"></div>
  <svg class="abs" style="left:560px;top:28px" width="70" height="440" viewBox="0 0 70 440"><path d="M0 1H59V432" fill="none" stroke="#999" stroke-width="2"/></svg>

  <div class="contact" style="top:80px">
    <div class="contact-icon"><svg width="20" height="20" viewBox="0 0 24 24" fill="none" stroke="#fff" stroke-width="2"><path d="M12 22s7-7 7-12a7 7 0 0 0-14 0c0 5 7 12 7 12z"/><circle cx="12" cy="10" r="2.5"/></svg></div>
    <div class="contact-text">Address :<br>175 , Lorem Ipsum Dolor , United States</div>
  </div>
  <div class="contact" style="top:186px">
    <div class="contact-icon"><svg width="20" height="20" viewBox="0 0 24 24" fill="none" stroke="#fff" stroke-width="2"><rect x="3" y="5" width="18" height="14" rx="1"/><path d="M3 6l9 7 9-7"/></svg></div>
    <div class="contact-text">Email Us :<br>info@maisonverlaine.com</div>
  </div>
  <div class="contact" style="top:287px">
    <div class="contact-icon"><svg width="20" height="20" viewBox="0 0 24 24" fill="none" stroke="#fff" stroke-width="2"><path d="M5 3h4l2 5-2.5 1.5a11 11 0 0 0 6 6L16 13l5 2v4a2 2 0 0 1-2 2A17 17 0 0 1 3 5a2 2 0 0 1 2-2z"/></svg></div>
    <div class="contact-text">Call Us :<br>+ 1 888 888 8888</div>
  </div>
  <div class="contact" style="top:388px">
    <div class="contact-icon"><svg width="20" height="20" viewBox="0 0 24 24" fill="none" stroke="#fff" stroke-width="2"><path d="M6 9V3h12v6"/><rect x="3" y="9" width="18" height="8" rx="1"/><path d="M6 14h12v7H6z"/></svg></div>
    <div class="contact-text">Call Us :<br>+ 1 999 999 9999</div>
  </div>
</section>

</body>
</html>
```